Professional modern business card design

A business card for my nutrition business, wanting a professional look, with info clearly visible. Open to using logo colours too.

Would like key info on the front -
logo
my name and qualifications
email
phone number

and just an enlarged logo again / image on the back.

```html
<!DOCTYPE html>
<html lang="en">
<head>
<meta charset="utf-8">
<title>Verda Nutrition – Business Card</title>
<link rel="stylesheet" href="https://fonts.googleapis.com/css2?family=Open+Sans:wght@400;700&display=swap">
<style>
  :root {
    --stage: #2b2b2d;
    --navy: #050a1f;
    --ink: #0d2a3d;
    --lime: #c4d124;
    --lime-deep: #b6c21e;
    --paper: #ffffff;
    --paper-shade: #eeeeee;
  }
  * { box-sizing: border-box; margin: 0; padding: 0; }
  html, body {
    width: 1200px; height: 900px; overflow: hidden;
    background: var(--stage);
    font-family: "Open Sans", sans-serif;
  }
  .card {
    position: absolute; left: 250px;
    width: 700px; height: 400px;
    overflow: hidden;
    box-shadow: 0 10px 30px rgba(0,0,0,.45);
  }
  .card--back { top: 40px; background: var(--navy); }
  .card--front { top: 460px; background: var(--paper); }

  .leaf-pattern { position: absolute; inset: 0; }
  .card--back .leaf-pattern {
    background: radial-gradient(circle at 50% 50%, #0a1230 0%, var(--navy) 70%);
  }
  .card--front .leaf-pattern {
    background: linear-gradient(120deg, var(--paper) 0%, #f7f7f7 60%, var(--paper-shade) 100%);
  }

  .brand {
    position: absolute;
    font-weight: 700;
    line-height: 1;
    white-space: nowrap;
  }
  .card--back .brand {
    left: 50%; top: 50%; transform: translate(-50%, -50%);
    font-size: 62px; color: var(--lime);
  }
  .card--front .brand {
    right: 40px; top: 118px;
    font-size: 44px; color: var(--ink);
    width: 260px; white-space: normal; line-height: 1.05;
  }

  .contact-panel {
    position: absolute; left: 0; top: 96px;
    width: 400px; height: 252px;
    background: linear-gradient(90deg, var(--lime-deep), var(--lime));
    border-radius: 0 30px 30px 0;
    padding: 62px 0 0 70px;
    color: var(--ink);
  }
  .person-name { font-size: 22px; font-weight: 400; letter-spacing: .5px; }
  .person-role { font-size: 17px; margin: 2px 0 0 10px; }
  .contact-list { list-style: none; margin: 26px 0 0 30px; }
  .contact-list li {
    display: flex; align-items: center; gap: 10px;
    font-size: 17px; line-height: 1.55;
  }
  .contact-list svg { width: 16px; height: 16px; flex: none; }
</style>
</head>
<body>

<section class="card card--back" aria-label="Card back">
  <div class="leaf-pattern" role="img" aria-label="Faint outlined herb and leaf pattern on navy"></div>
  <div class="brand">Verda Nutrition</div>
</section>

<section class="card card--front" aria-label="Card front">
  <div class="leaf-pattern" role="img" aria-label="Light grey outlined herb and leaf pattern on white"></div>

  <div class="contact-panel">
    <p class="person-name">MARA ELLISON</p>
    <p class="person-role">Director</p>
    <ul class="contact-list">
      <li>
        <svg viewBox="0 0 16 16" aria-hidden="true"><rect x="4" y="1" width="8" height="14" rx="1.5" fill="none" stroke="currentColor" stroke-width="1.4"/><line x1="7" y1="12.5" x2="9" y2="12.5" stroke="currentColor" stroke-width="1.2"/></svg>
        555-014-2298
      </li>
      <li>
        <svg viewBox="0 0 16 16" aria-hidden="true"><rect x="1" y="3.5" width="14" height="10" rx="1" fill="currentColor"/><path d="M1.5 4 L8 9 L14.5 4" fill="none" stroke="#c4d124" stroke-width="1.3"/></svg>
        mara@verdanutrition.com
      </li>
    </ul>
  </div>

  <div class="brand">Verda Nutrition</div>
</section>

</body>
</html>
```